Corvale Fitouts Web

We just need an update/re-design of our existing web site that would include our new company logo and some new photo's. Our current web site can be viewed at www.corvalefitouts.com.au. We would require something very similar to what we have at the moment in terms of content it should all be the same.
The web site would basically act more as a portfolio than one that would generate more business.
We are after a very modern and simple design and maybe something where we can upload our own project photo's and project descriptions as we complete them.

```html
<!DOCTYPE html>
<html lang="en">
<head>
<meta charset="utf-8">
<title>Corvale Fitouts</title>
<link href="https://fonts.googleapis.com/css2?family=Lato:wght@300;400;700&family=Open+Sans:wght@400&family=Roboto:wght@400&display=swap" rel="stylesheet">
<style>
  :root {
    --black: #000;
    --steel: #4a7895;
    --steel-deep: #1e5672;
    --steel-line: #2f6a88;
    --text-muted: #a9a9a9;
    --text-light: #d4d4d4;
    --white: #fff;
    --logo-grey: #8c8c8c;
  }
  * { margin: 0; padding: 0; box-sizing: border-box; }
  html, body { width: 1200px; height: 1070px; overflow: hidden; background: var(--black); }
  body { position: relative; font-family: "Open Sans", sans-serif; }

  .site-header { position: absolute; left: 0; top: 0; width: 1200px; height: 125px; background: var(--black); }
  .brand { position: absolute; left: 122px; top: 22px; font-family: "Lato", sans-serif; font-weight: 300; font-size: 38px; color: var(--logo-grey); letter-spacing: 0.5px; }

  .main-nav { position: absolute; left: 120px; top: 84px; height: 41px; display: flex; }
  .main-nav a { display: block; height: 41px; line-height: 44px; padding: 0 30px; font-family: "Roboto", sans-serif; font-size: 11px; letter-spacing: 1.2px; color: var(--white); text-decoration: none; text-transform: uppercase; }
  .main-nav a.is-active { background: var(--steel); padding: 0 24px; }
  .main-nav .divider { width: 1px; height: 26px; margin-top: 10px; background: #555; }

  .search { position: absolute; left: 865px; top: 92px; width: 196px; height: 26px; background: var(--white); border-radius: 4px; border: 1px solid #ccc; }
  .search span { position: absolute; left: 12px; top: 5px; font-family: Georgia, serif; font-style: italic; font-size: 11px; color: #aaa; }
  .search svg { position: absolute; right: 8px; top: 5px; }

  .hero-band { position: absolute; left: 0; top: 125px; width: 1200px; height: 498px;
    background: linear-gradient(90deg, #5b2414 0%, #8b3a20 30%, #6e2b17 60%, #8a3a1f 85%, #5a2313 100%); }
  .hero-frame { position: absolute; left: 120px; top: 125px; width: 960px; height: 498px; background: var(--steel); padding: 7px 6px 5px 6px; }
  .hero-photo { width: 100%; height: 100%;
    background: linear-gradient(160deg, #2b2f36 0%, #3b3f46 20%, #d9d8d4 45%, #c8c2b6 70%, #8d8779 100%); }

  .content { position: absolute; left: 0; top: 623px; width: 1200px; height: 360px; background: var(--black); }
  .about { position: absolute; left: 128px; top: 24px; width: 580px; }
  .about h1 { font-family: "Lato", sans-serif; font-weight: 700; font-size: 20px; color: var(--white); margin-bottom: 13px; }
  .about p, .about li { font-size: 13.5px; line-height: 20px; color: var(--text-muted); padding-left: 3px; }
  .about ul { list-style: none; padding-left: 24px; }
  .about li { color: var(--text-light); }
  .about li::before { content: ">"; margin-right: 8px; }

  .projects { position: absolute; left: 732px; top: 0; width: 348px; height: 360px; background: var(--steel); }
  .projects h2 { position: absolute; left: 27px; top: 24px; font-family: "Lato", sans-serif; font-weight: 700; font-size: 20px; color: var(--white); }
  .thumb { position: absolute; left: 29px; width: 280px; height: 72px; border: 2px solid var(--white); }
  .thumb-1 { top: 65px; background: linear-gradient(180deg, #2a2a2a 0%, #9a9a96 50%, #d6d6d2 100%); }
  .thumb-2 { top: 149px; background: linear-gradient(180deg, #5d86b0 0%, #8fb0cf 45%, #4a3b33 75%, #9b9690 100%); }
  .thumb-3 { top: 233px; background: linear-gradient(180deg, #7e98ad 0%, #6a6a6a 40%, #8f5a3a 65%, #b9b9b4 100%); }
  .scroll-track { position: absolute; left: 330px; top: 65px; width: 2px; height: 240px; background: var(--white); }
  .scroll-thumb { position: absolute; left: 330px; top: 134px; width: 3px; height: 41px; background: #1c2e3a; }

  .site-footer { position: absolute; left: 0; top: 983px; width: 1200px; height: 87px; background: var(--steel-deep); border-top: 2px solid var(--steel-line); }
  .footer-brand { position: absolute; left: 130px; top: 28px; font-family: "Lato", sans-serif; font-weight: 300; font-size: 20px; color: #7e9aa9; }
  .footer-contact { position: absolute; right: 120px; top: 22px; text-align: right; font-family: "Lato", sans-serif; font-size: 10px; line-height: 15px; color: var(--white); }
</style>
</head>
<body>
  <header class="site-header">
    <div class="brand">Corvale Fitouts</div>
    <nav class="main-nav">
      <a href="#">Home</a>
      <a href="#" class="is-active">Recent Projects</a>
      <a href="#">Our Services</a>
      <span class="divider"></span>
      <a href="#">Contact Us</a>
    </nav>
    <div class="search">
      <span>Search</span>
      <svg width="14" height="14" viewBox="0 0 14 14"><circle cx="5.5" cy="5.5" r="4" fill="none" stroke="#aaa" stroke-width="1.6"/><line x1="8.5" y1="8.5" x2="12.5" y2="12.5" stroke="#aaa" stroke-width="2"/></svg>
    </div>
  </header>

  <div class="hero-band" role="img" aria-label="Warm wood grain panelling backdrop"></div>
  <div class="hero-frame">
    <div class="hero-photo" role="img" aria-label="Office lobby interior with felt ceiling baffles, timber battens, staircase and lift"></div>
  </div>

  <main class="content">
    <section class="about">
      <h1>Corvale Fitouts Pty Limited</h1>
      <p>Corvale Fitouts Pty Ltd was established in 2005 and has been operating in the Sydney area, but has completed numerous projects outside of Sydney.<br>We specialise in the internal fit outs to,</p>
      <ul>
        <li>Industrial Offices</li>
        <li>Multi Storey Offices</li>
        <li>Commercial Projects</li>
        <li>Residential Houses</li>
        <li>External Facades</li>
      </ul>
      <p>The key group of our operating staff have all been involved in the construction industry for well over 20 years.&nbsp; Our employees are skilled and trained and have the experience to deliver the best possible product, safely and on time. At Corvale Fitouts we pride ourselves on working together with our clients in providing the best possible service on schedule and within budget</p>
    </section>
    <aside class="projects">
      <h2>Recent Projects</h2>
      <div class="thumb thumb-1" role="img" aria-label="Modern office building exterior with cantilevered upper level"></div>
      <div class="thumb thumb-2" role="img" aria-label="Glass facade office building under blue sky"></div>
      <div class="thumb thumb-3" role="img" aria-label="Commercial building front with timber cladding panels"></div>
      <div class="scroll-track"></div>
      <div class="scroll-thumb"></div>
    </aside>
  </main>

  <footer class="site-footer">
    <div class="footer-brand">Corvale Fitouts</div>
    <div class="footer-contact">
      418 Harlow Street, Parramatta NSW<br>
      Tel: 0800-555-017, 1800-555-392<br>
      Email: info@corvalefitouts.com
    </div>
  </footer>
</body>
</html>
```